Dr. Pell Works
Business card, stationary, fax page, envelope
Dr. Pell Works - Corporate Services
Creative Brief
Bright & Fun-filled
Grant Bevis Hallworth
Senior Account Executive
417 S. Tavish Ave Los Angeles CA 90012
grant@drpellworks.example
drpellworks.example
I also have 4 other people that need their won business cards but with their cell phone and title info.

```html
<!DOCTYPE html>
<html lang="en">
<head>
<meta charset="utf-8">
<title>Dr. Pell Works — Stationery Set</title>
<link href="https://fonts.googleapis.com/css2?family=Montserrat:wght@400;700&family=Open+Sans:wght@400;600&display=swap" rel="stylesheet">
<style>
  :root {
    --yellow: #f5c400;
    --ink: #1b1b1b;
    --paper: #ffffff;
    --grey: #8a8a8a;
    --rule: #d9d9d9;
    --stage: #e6e6e4;
    --faint: #efeae0;
  }
  * { box-sizing: border-box; margin: 0; padding: 0; }
  html, body { width: 1200px; height: 929px; overflow: hidden; }
  body { background: var(--stage); font-family: "Open Sans", sans-serif; color: var(--ink); position: relative; }

  .sheet { position: absolute; background: var(--paper); box-shadow: 0 4px 14px rgba(0,0,0,.18); overflow: hidden; }

  .brand { display: flex; align-items: center; gap: 8px; }
  .brand-dot { width: 22px; height: 22px; border-radius: 50%; background: var(--yellow); flex: none; }
  .brand-name { font-family: "Montserrat", sans-serif; font-weight: 700; font-size: 13px; color: var(--ink); white-space: nowrap; }
  .brand.on-dark .brand-name { color: var(--paper); }

  .mascot-fill { position: absolute; border-radius: 50%; background: radial-gradient(circle, var(--faint) 0%, rgba(239,234,224,0) 72%); }

  .yellow-rule { position: absolute; left: 0; right: 0; bottom: 0; height: 6px; background: var(--yellow); }
  .footer-line { position: absolute; left: 24px; right: 24px; bottom: 14px; font-size: 6.5px; color: var(--grey); text-align: center; }

  /* Letterhead */
  .letterhead { left: 40px; top: 40px; width: 300px; height: 424px; }
  .letterhead .brand { position: absolute; left: 24px; top: 24px; }
  .letterhead .mascot-fill { left: 70px; top: 150px; width: 200px; height: 200px; }
  .letter-body { position: absolute; left: 24px; top: 84px; right: 30px; font-size: 7.5px; line-height: 1.7; color: #444; }
  .letter-body p { margin-bottom: 8px; }

  /* Fax */
  .fax { left: 370px; top: 40px; width: 300px; height: 424px; }
  .fax .brand { position: absolute; left: 24px; top: 24px; }
  .fax-title { position: absolute; right: 24px; top: 22px; font-family: "Montserrat", sans-serif; font-weight: 700; font-size: 26px; letter-spacing: 3px; }
  .fax-fields { position: absolute; left: 24px; right: 24px; top: 84px; list-style: none; }
  .fax-fields li { display: flex; align-items: flex-end; gap: 8px; height: 26px; border-bottom: 1px solid var(--rule); font-size: 8px; font-weight: 600; }
  .fax-checks { position: absolute; left: 24px; top: 230px; display: flex; gap: 22px; font-size: 8px; }
  .fax-checks span { display: flex; align-items: center; gap: 5px; }
  .fax-checks i { width: 9px; height: 9px; border: 1px solid var(--ink); display: inline-block; }
  .fax .mascot-fill { left: 90px; top: 260px; width: 160px; height: 160px; }

  /* Envelopes */
  .envelope { left: 700px; top: 40px; width: 460px; height: 230px; }
  .envelope .brand { position: absolute; left: 22px; top: 22px; }
  .envelope .return { position: absolute; left: 52px; top: 48px; font-size: 7px; color: var(--grey); line-height: 1.5; }
  .envelope .mascot-fill { left: 150px; top: 40px; width: 160px; height: 160px; }
  .envelope .yellow-rule { height: 8px; }

  .envelope-back { left: 700px; top: 300px; width: 460px; height: 230px; }
  .envelope-back svg { position: absolute; inset: 0; }

  /* Cards */
  .card { top: 580px; width: 315px; height: 180px; }
  .card-front { left: 40px; }
  .card-front .brand { position: absolute; left: 22px; top: 22px; }
  .card-front .mascot-fill { right: -30px; top: 30px; width: 160px; height: 160px; left: auto; }
  .card-person { position: absolute; left: 22px; top: 82px; }
  .card-name { font-family: "Montserrat", sans-serif; font-weight: 700; font-size: 11px; }
  .card-title { font-size: 8px; color: var(--yellow); font-weight: 600; margin-bottom: 8px; background: var(--ink); display: inline-block; padding: 1px 5px; }
  .card-contact { font-size: 7.5px; line-height: 1.6; color: #444; }

  .card-dark { left: 420px; background: var(--ink); }
  .card-dark .brand { position: absolute; left: 22px; top: 22px; }
  .card-dark .card-person { top: 82px; }
  .card-dark .card-name { color: var(--paper); }
  .card-dark .card-contact { color: #cfcfcf; }
  .card-dark .yellow-rule { height: 5px; }

  .card-split { left: 800px; background: var(--yellow); }
  .card-split .half { position: absolute; left: 0; right: 0; bottom: 0; height: 50%; background: var(--ink); }
  .card-split .brand { position: absolute; left: 50%; top: 50%; transform: translate(-50%, -50%); }
  .card-split .brand-dot { width: 40px; height: 40px; background: var(--paper); }
</style>
</head>
<body>

  <section class="sheet letterhead">
    <div class="brand"><span class="brand-dot"></span><span class="brand-name">Dr. Pell Works</span></div>
    <div class="mascot-fill" role="img" aria-label="Faint mascot illustration as page watermark"></div>
    <div class="letter-body">
      <p>Client Name<br>Street Address</p>
      <p>Dear Client,</p>
      <p>Thank you for choosing our team this season.<br>We look forward to working with you soon.</p>
      <p>Kind regards,<br>Grant Bevis Hallworth</p>
    </div>
    <p class="footer-line">417 S. Tavish Ave Los Angeles CA 90012 · drpellworks.example</p>
    <div class="yellow-rule"></div>
  </section>

  <section class="sheet fax">
    <div class="brand"><span class="brand-dot"></span><span class="brand-name">Dr. Pell Works</span></div>
    <h1 class="fax-title">FAX</h1>
    <ul class="fax-fields">
      <li>To:</li><li>From:</li><li>Date:</li><li>Pages:</li><li>Re:</li>
    </ul>
    <div class="fax-checks">
      <span><i></i>Urgent</span><span><i></i>Review</span><span><i></i>Reply</span>
    </div>
    <div class="mascot-fill" role="img" aria-label="Faint mascot illustration as page watermark"></div>
    <p class="footer-line">417 S. Tavish Ave Los Angeles CA 90012 · drpellworks.example</p>
    <div class="yellow-rule"></div>
  </section>

  <section class="sheet envelope">
    <div class="brand"><span class="brand-dot"></span><span class="brand-name">Dr. Pell Works</span></div>
    <p class="return">417 S. Tavish Ave<br>Los Angeles CA 90012</p>
    <div class="mascot-fill" role="img" aria-label="Faint mascot illustration on envelope front"></div>
    <div class="yellow-rule"></div>
  </section>

  <section class="sheet envelope-back">
    <svg viewBox="0 0 460 230" width="460" height="230" aria-hidden="true">
      <path d="M0 0 H460 V20 C330 40 260 150 0 120 Z" fill="var(--ink)"/>
      <path d="M0 0 H210 C150 20 80 40 0 60 Z" fill="var(--yellow)"/>
      <path d="M0 120 C260 150 330 40 460 20" fill="none" stroke="var(--yellow)" stroke-width="4"/>
      <path d="M0 230 L230 135 L460 230" fill="none" stroke="var(--rule)" stroke-width="1"/>
    </svg>
  </section>

  <section class="sheet card card-front">
    <div class="brand"><span class="brand-dot"></span><span class="brand-name">Dr. Pell Works</span></div>
    <div class="mascot-fill" role="img" aria-label="Faint mascot illustration on card"></div>
    <div class="card-person">
      <p class="card-name">Grant Bevis Hallworth</p>
      <p class="card-title">Senior Account Executive</p>
      <p class="card-contact">417 S. Tavish Ave Los Angeles CA 90012<br>grant@drpellworks.example<br>drpellworks.example</p>
    </div>
  </section>

  <section class="sheet card card-dark">
    <div class="brand on-dark"><span class="brand-dot"></span><span class="brand-name">Dr. Pell Works</span></div>
    <div class="card-person">
      <p class="card-name">Grant Bevis Hallworth</p>
      <p class="card-title">Senior Account Executive</p>
      <p class="card-contact">417 S. Tavish Ave Los Angeles CA 90012<br>grant@drpellworks.example<br>drpellworks.example</p>
    </div>
    <div class="yellow-rule"></div>
  </section>

  <section class="sheet card card-split">
    <div class="half"></div>
    <div class="brand"><span class="brand-dot"></span></div>
  </section>

</body>
</html>
```